Teiwana Eliquid packaging design

Hi Guys!
We're looking for a new design for our eliquid.
We will have 7 flavors in this line and will be using the seven colors of the chakras.
We would like to keep the design clean, fresh yet bold.
I have a poorly drawn concept attached for you guys to make look AWESOME.
The line that runs up the left hand side of the box / label will be the same color as one of the 7 segments of the circle to the right.
These colors will represent the flavor profile of the liquid, as such i would like to see one segment of the lot BOLD, the others a bit greyed out.. Feel free to play around with the sizing and description.
The brand name will be Teiwana (or maori for "love") - I'm unsure where to place that or how it is to be written, but again, we would like to keep it fresh and clean - i dont mind the inclusion of a koru to convey NZ or water droplets to convey the fresh feel.
All the flavors will be fruity
the label / box will need to contain the following:
- "WARNING: This product contains Nicotine. Nicotine is an addictive chemical" (in the same style as a cigarette packet) - front and center
- 60ml somewhere (which is the bottle size)
- 3mg/ml somewhere (nicotine strength)
Flavor description (for the violet one - Mixed berry punch, yellow - mango guava, green- apples, red - strawberry rhubarb, yellow - pineapple / pina colada etc)
- on the sides: Ingredients: Vegetable Glycerin. Proplyene Glycol, Natural and artifical flavors, Nicotine (unless 0mg)
- warning prop 65: This product contains a chemcial known to the state of California to cause cancer and other reproductive harm
- Must be of legal smoking age to use this product. Not for sale to minors. Not for pregnant or breastfeeding women. Keep out of reach of children and pets.
- an 18+ sticker somewhere
- Barcode / batch number
- Proudly made in New Zealand with Love (Teiwana)
And anything else you guys can think of which would make it look awesome!
The bottle style will be 60ml "Tidy Heron" bottles :)
-

```html
<!DOCTYPE html>
<html lang="en">
<head>
<meta charset="utf-8">
<title>Teiwana E-liquid Labels</title>
<link rel="stylesheet" href="https://fonts.googleapis.com/css2?family=Montserrat:wght@400;500&family=Open+Sans:wght@400;600&display=swap">
<style>
  :root{
    --stage:#b4b4b6;
    --paper:#ffffff;
    --ink:#1a1a1a;
    --grey:#4a4a4a;
    --text:#555555;
    --apple:#22e61e;
    --berry:#4a3ccc;
    --label-scale:1.18;
  }
  *{box-sizing:border-box;margin:0;padding:0}
  html,body{width:966px;height:1200px;overflow:hidden}
  body{background:var(--stage);position:relative;font-family:"Open Sans",sans-serif;color:var(--text)}

  .label-slot{position:absolute}
  .label-slot.apples{left:296px;top:34px;width:375px;height:549px}
  .label-slot.berry{left:161px;top:617px;width:644px;height:549px}

  .label{position:absolute;left:0;top:0;height:465px;background:var(--paper);
    transform:scale(var(--label-scale));transform-origin:0 0}
  .label.apples{width:318px;--flavour:var(--apple)}
  .label.berry{width:546px;--flavour:var(--berry)}

  .side-panel{position:absolute;top:0;width:150px}
  .apples .side-panel{left:11px}
  .berry .side-panel{left:69px}

  .brand-name{font-family:"Montserrat",sans-serif;font-weight:400;font-size:24px;letter-spacing:1px;color:var(--grey);margin:22px 0 0 6px;line-height:1}
  .ingredients,.age-notice{font-size:9.3px;line-height:1.16;color:var(--text)}
  .ingredients{margin-top:12px}
  .age-badge{width:27px;height:27px;border-radius:50%;background:var(--ink);color:#fff;font-weight:600;font-size:12px;display:flex;align-items:center;justify-content:center;margin:6px 0 6px 53px}
  .brand-mark{display:flex;align-items:center;justify-content:center;gap:6px;margin-top:24px;width:140px}
  .brand-mark .dot{width:12px;height:12px;border-radius:50%;background:var(--grey)}
  .brand-mark span{font-family:"Montserrat",sans-serif;font-size:15px;color:var(--grey);letter-spacing:1px}
  .origin{width:140px;text-align:center;font-size:9.6px;letter-spacing:1px;line-height:1.1;color:var(--ink);margin-top:30px}
  .prop-warning{position:absolute;top:405px;width:84px;height:43px;border:1px solid #999;padding:2px 3px;text-align:center}
  .apples .prop-warning{left:37px}
  .berry .prop-warning{left:96px}
  .prop-warning strong{display:block;font-size:8px;font-weight:400;border-bottom:1px solid #999;color:var(--grey)}
  .prop-warning p{font-size:4.6px;line-height:1.2;margin-top:2px}

  .flavour-line{position:absolute;left:0;top:0;pointer-events:none}
  .flavour-wheel{position:absolute;width:46px;height:46px}
  .apples .flavour-wheel{left:260px;top:32px}
  .berry .flavour-wheel{left:431px;top:35px}

  .vertical{position:absolute;writing-mode:vertical-rl;transform:rotate(180deg);white-space:nowrap}
  .wordmark{font-family:"Montserrat",sans-serif;font-weight:400;font-size:42px;letter-spacing:2px;color:var(--grey);line-height:1}
  .apples .wordmark{left:258px;top:86px}
  .berry .wordmark{left:431px;top:88px}
  .flavour-name{font-family:"Montserrat",sans-serif;font-weight:500;font-size:15px;letter-spacing:1.5px;color:var(--grey);line-height:1;bottom:165px}
  .apples .flavour-name{left:190px}
  .berry .flavour-name{left:362px}
  .strength{position:absolute;top:306px;font-size:10px;color:var(--grey)}
  .apples .strength{left:203px}
  .berry .strength{left:375px}

  .health-warning{position:absolute;top:326px;width:157px;height:137px;border:2px solid var(--ink);background:var(--paper);
    display:flex;flex-direction:column;align-items:center;justify-content:center;text-align:center;color:var(--ink)}
  .apples .health-warning{left:160px;font-size:11.2px;line-height:1.45}
  .berry .health-warning{left:331px;font-size:14.5px;line-height:1.5}
  .health-warning strong{font-weight:600}
</style>
</head>
<body>

<div class="label-slot apples">
  <section class="label apples">
    <div class="side-panel">
      <h1 class="brand-name">TEIWANA</h1>
      <p class="ingredients">Ingredients:<br>Vegetable Glycerin. Proplyene Glycol, Natural and artifical flavors, Nicotine (unless 0mg)</p>
      <div class="age-badge">18+</div>
      <p class="age-notice">Must be of legal smoking age to use this product.<br>Not for sale to minors.<br>Not for pregnant or breastfeeding women.<br>Keep out of reach of children and pets.</p>
      <div class="brand-mark"><i class="dot"></i><span>Teiwana</span></div>
      <p class="origin">Proudly made in<br>New Zealand<br>with Love (Teiwana)</p>
    </div>
    <div class="prop-warning"><strong>&#9888; WARNING</strong><p>This product contains a chemical known to the state of California to cause cancer and other reproductive harm</p></div>

    <svg class="flavour-line" width="318" height="465" viewBox="0 0 318 465"><path d="M177 326 V46 Q177 18 205 18 H318" fill="none" stroke="var(--apple)" stroke-width="8"/></svg>
    <svg class="flavour-wheel" viewBox="0 0 46 46" role="img" aria-label="Flavour profile wheel, green segment bold">
      <g transform="rotate(-90 23 23)" fill="none" stroke-width="22">
        <circle cx="23" cy="23" r="11" stroke="#8b7cf0" stroke-opacity=".45" stroke-dasharray="9.874 69.115" stroke-dashoffset="0"/>
        <circle cx="23" cy="23" r="11" stroke="#7aa0f0" stroke-opacity=".45" stroke-dasharray="9.874 69.115" stroke-dashoffset="-9.874"/>
        <circle cx="23" cy="23" r="11" stroke="var(--apple)" stroke-dasharray="9.874 69.115" stroke-dashoffset="-19.748"/>
        <circle cx="23" cy="23" r="11" stroke="#7ee07a" stroke-opacity=".45" stroke-dasharray="9.874 69.115" stroke-dashoffset="-29.622"/>
        <circle cx="23" cy="23" r="11" stroke="#f3ea6a" stroke-opacity=".45" stroke-dasharray="9.874 69.115" stroke-dashoffset="-39.496"/>
        <circle cx="23" cy="23" r="11" stroke="#f6a65a" stroke-opacity=".45" stroke-dasharray="9.874 69.115" stroke-dashoffset="-49.37"/>
        <circle cx="23" cy="23" r="11" stroke="#f27a7a" stroke-opacity=".45" stroke-dasharray="9.874 69.115" stroke-dashoffset="-59.244"/>
      </g>
    </svg>
    <div class="vertical wordmark">TEIWANA</div>
    <div class="vertical flavour-name">APPLES</div>
    <p class="strength">60 ml | 3mg/ml</p>
    <div class="health-warning"><strong>WARNING:</strong>This product contains<br>Nicotine.<br>Nicotine is an addictive<br>chemical</div>
  </section>
</div>

<div class="label-slot berry">
  <section class="label berry">
    <div class="side-panel">
      <h1 class="brand-name">TEIWANA</h1>
      <p class="ingredients">Ingredients:<br>Vegetable Glycerin. Proplyene Glycol, Natural and artifical flavors, Nicotine (unless 0mg)</p>
      <div class="age-badge">18+</div>
      <p class="age-notice">Must be of legal smoking age to use this product.<br>Not for sale to minors.<br>Not for pregnant or breastfeeding women.<br>Keep out of reach of children and pets.</p>
      <div class="brand-mark"><i class="dot"></i><span>Teiwana</span></div>
      <p class="origin">Proudly made in<br>New Zealand<br>with Love (Teiwana)</p>
    </div>
    <div class="prop-warning"><strong>&#9888; WARNING</strong><p>This product contains a chemical known to the state of California to cause cancer and other reproductive harm</p></div>

    <svg class="flavour-line" width="546" height="465" viewBox="0 0 546 465"><path d="M348 326 V50 Q348 22 376 22 H489" fill="none" stroke="var(--berry)" stroke-width="8"/></svg>
    <svg class="flavour-wheel" viewBox="0 0 46 46" role="img" aria-label="Flavour profile wheel, violet segment bold">
      <g transform="rotate(-90 23 23)" fill="none" stroke-width="22">
        <circle cx="23" cy="23" r="11" stroke="var(--berry)" stroke-dasharray="9.874 69.115" stroke-dashoffset="0"/>
        <circle cx="23" cy="23" r="11" stroke="#7aa0f0" stroke-opacity=".45" stroke-dasharray="9.874 69.115" stroke-dashoffset="-9.874"/>
        <circle cx="23" cy="23" r="11" stroke="#8fb4f2" stroke-opacity=".45" stroke-dasharray="9.874 69.115" stroke-dashoffset="-19.748"/>
        <circle cx="23" cy="23" r="11" stroke="#7ee07a" stroke-opacity=".45" stroke-dasharray="9.874 69.115" stroke-dashoffset="-29.622"/>
        <circle cx="23" cy="23" r="11" stroke="#f3ea6a" stroke-opacity=".45" stroke-dasharray="9.874 69.115" stroke-dashoffset="-39.496"/>
        <circle cx="23" cy="23" r="11" stroke="#f6a65a" stroke-opacity=".45" stroke-dasharray="9.874 69.115" stroke-dashoffset="-49.37"/>
        <circle cx="23" cy="23" r="11" stroke="#f27a7a" stroke-opacity=".45" stroke-dasharray="9.874 69.115" stroke-dashoffset="-59.244"/>
      </g>
    </svg>
    <div class="vertical wordmark">TEIWANA</div>
    <div class="vertical flavour-name">MIXED BERRY PUNCH</div>
    <p class="strength">60 ml | 3mg/ml</p>
    <div class="health-warning"><strong>WARNING:</strong>This product<br>contains Nicotine.<br>Nicotine is an<br>addictive chemical</div>
  </section>
</div>

</body>
</html>
```